Virtual Assistant/Online Marketing Business Card/Stationary

I need a professional but modern business card/stationary for my company in Dallas called Brivolo. Brivolo is a virtual assistant specializing in online marketing. I would like a unique design that stands out and makes my brand clear. Incorporating the logo is a must and have attached it to this brief.

Target Market(s)

small business owners & entrepreneurs, 35-65

Industry/Entity Type

Business

Contact Information for Business Card

Maren Tolk
marentolk@brivolo.biz
(555) 271-9064
brivolo.biz

Font styles to use
Sans Serif

Colors
f04a50
3176b5
9bcb3c

Requirements
Must have
• Colors that match the logo colors. Logo integration

```html
<!DOCTYPE html>
<html lang="en">
<head>
<meta charset="utf-8">
<title>Brivolo Stationery</title>
<link href="https://fonts.googleapis.com/css2?family=Arimo:wght@400;700&display=swap" rel="stylesheet">
<style>
  :root {
    --backdrop: #e9e9e7;
    --paper: #ffffff;
    --envelope-tint: #f8eeee;
    --teal: #3a9aa3;
    --red: #b83227;
    --green: #6ab833;
    --ink: #1b1b1b;
    --shadow: 0 2px 6px rgba(0,0,0,0.12), 0 10px 24px rgba(0,0,0,0.08);
  }
  * { box-sizing: border-box; margin: 0; padding: 0; }
  html, body { width: 1200px; height: 900px; overflow: hidden; }
  body {
    background: var(--backdrop);
    font-family: "Arimo", Arial, sans-serif;
    color: var(--ink);
    position: relative;
  }
  .sheet {
    position: absolute;
    background: var(--paper);
    box-shadow: var(--shadow);
    overflow: hidden;
  }
  .wordmark {
    font-weight: 700;
    color: var(--ink);
    letter-spacing: -0.5px;
    line-height: 1;
  }
  .contact-list { list-style: none; font-weight: 700; line-height: 1.35; }
  .contact-list li { display: flex; align-items: center; gap: 5px; }
  .contact-list svg { flex: none; }
  .corner-wash { position: absolute; }

  /* Letterhead */
  .letterhead { left: 60px; top: 140px; width: 440px; height: 622px; }
  .letterhead .wordmark { position: absolute; left: 40px; top: 44px; font-size: 40px; }
  .letterhead .contact-list { position: absolute; left: 40px; bottom: 40px; font-size: 13px; }
  .letterhead .corner-wash {
    right: 0; bottom: 0; width: 250px; height: 330px;
    background: linear-gradient(135deg, rgba(106,184,51,0) 20%, rgba(106,184,51,0.14) 45%, rgba(184,50,39,0.12) 65%, rgba(58,154,163,0.14) 85%);
    clip-path: polygon(100% 0, 100% 100%, 0 100%);
  }

  /* Envelope front */
  .envelope-front { left: 560px; top: 50px; width: 560px; height: 260px; background: var(--envelope-tint); }
  .envelope-front .wordmark { position: absolute; left: 28px; top: 26px; font-size: 30px; background: var(--paper); padding: 8px 10px; }
  .envelope-front .contact-list { position: absolute; left: 30px; top: 82px; font-size: 10px; }
  .envelope-front .corner-wash {
    right: 0; top: 0; width: 170px; height: 260px;
    background: linear-gradient(160deg, rgba(106,184,51,0.14) 20%, rgba(184,50,39,0.14) 55%, rgba(58,154,163,0.16) 85%);
    clip-path: polygon(100% 0, 100% 100%, 0 100%);
  }

  /* Envelope back */
  .envelope-back { left: 560px; top: 340px; width: 560px; height: 260px; }
  .envelope-back .flap {
    position: absolute; left: 0; top: 0; width: 100%; height: 74px;
    background: var(--teal);
    border-radius: 0 0 22px 22px;
  }

  /* Business cards */
  .card { width: 270px; height: 165px; top: 650px; }
  .card-back { left: 560px; background: var(--teal); }
  .card-back .handle {
    position: absolute; display: flex; align-items: center; gap: 5px;
    font-size: 9px; font-weight: 700; color: var(--ink);
  }
  .card-back .handle i { display: block; width: 10px; height: 10px; background: var(--paper); }
  .card-back .handle-left { left: 12px; bottom: 12px; }
  .card-back .handle-right { right: 12px; top: 118px; }

  .card-front { left: 850px; }
  .card-front .wordmark { position: absolute; left: 18px; top: 34px; font-size: 26px; }
  .card-front .person { position: absolute; left: 20px; top: 86px; font-size: 12px; font-weight: 700; }
  .card-front .contact-list { position: absolute; right: 12px; bottom: 30px; font-size: 7px; }
  .card-front .corner-wash {
    right: 0; top: 0; width: 150px; height: 165px;
    background: linear-gradient(150deg, var(--green) 0%, var(--red) 45%, var(--teal) 90%);
    clip-path: polygon(30% 0, 100% 0, 100% 40%, 20% 100%, 0 100%);
    opacity: 0.9;
  }
</style>
</head>
<body>

  <section class="sheet letterhead">
    <div class="wordmark">Brivolo</div>
    <div class="corner-wash" role="img" aria-label="Soft corner wash in the brand green, red and teal"></div>
    <ul class="contact-list">
      <li><svg width="12" height="12" viewBox="0 0 12 12"><circle cx="6" cy="6" r="5.5" fill="none" stroke="#6ab833" stroke-width="1.4"/><path d="M4 3.5 L5.2 3.5 L5.6 5 L4.9 5.6 Q5.6 7 6.9 7.6 L7.5 6.9 L9 7.3 L9 8.5 Q6 9 3.8 5 Z" fill="#6ab833"/></svg>(555) 271-9064</li>
      <li><svg width="12" height="12" viewBox="0 0 12 12"><circle cx="6" cy="6" r="5.5" fill="#b83227"/><path d="M0.5 6 H11.5 M6 0.5 V11.5 M6 0.5 Q2.5 6 6 11.5 M6 0.5 Q9.5 6 6 11.5" stroke="#fff" stroke-width="0.8" fill="none"/></svg>brivolo.biz</li>
      <li><svg width="12" height="12" viewBox="0 0 12 12"><rect x="0.5" y="2.5" width="11" height="7.5" fill="#3a9aa3"/><path d="M0.5 2.5 L6 7 L11.5 2.5" stroke="#fff" stroke-width="0.9" fill="none"/></svg>marentolk@brivolo.biz</li>
    </ul>
  </section>

  <section class="sheet envelope-front">
    <div class="wordmark">Brivolo</div>
    <div class="corner-wash" role="img" aria-label="Soft corner wash in the brand green, red and teal"></div>
    <ul class="contact-list">
      <li><svg width="9" height="9" viewBox="0 0 12 12"><circle cx="6" cy="6" r="5.5" fill="none" stroke="#6ab833" stroke-width="1.6"/></svg>(555) 271-9064</li>
      <li><svg width="9" height="9" viewBox="0 0 12 12"><circle cx="6" cy="6" r="5.5" fill="#b83227"/></svg>brivolo.biz</li>
      <li><svg width="9" height="9" viewBox="0 0 12 12"><rect x="0.5" y="2.5" width="11" height="7.5" fill="#3a9aa3"/><path d="M0.5 2.5 L6 7 L11.5 2.5" stroke="#fff" stroke-width="0.9" fill="none"/></svg>marentolk@brivolo.biz</li>
    </ul>
  </section>

  <section class="sheet envelope-back">
    <div class="flap"></div>
  </section>

  <section class="sheet card card-back">
    <div class="handle handle-left"><i></i>brivolo</div>
    <div class="handle handle-right"><i></i>brivolo</div>
  </section>

  <section class="sheet card card-front">
    <div class="wordmark">Brivolo</div>
    <div class="person">Maren Tolk</div>
    <div class="corner-wash" role="img" aria-label="Bold corner panel in the brand green, red and teal"></div>
    <ul class="contact-list">
      <li><svg width="6" height="6" viewBox="0 0 12 12"><circle cx="6" cy="6" r="5" fill="none" stroke="#6ab833" stroke-width="2"/></svg>(555) 271-9064</li>
      <li><svg width="6" height="6" viewBox="0 0 12 12"><circle cx="6" cy="6" r="5.5" fill="#b83227"/></svg>brivolo.biz</li>
      <li><svg width="6" height="6" viewBox="0 0 12 12"><rect x="0.5" y="2.5" width="11" height="7.5" fill="#3a9aa3"/></svg>marentolk@brivolo.biz</li>
    </ul>
  </section>

</body>
</html>
```